The Velvet Heron Business Card

Looking for new business cards for our Directors and Manager
I have attached what they are currently, they are also gold foiled where you see gold sections. We do want them to be quite special and exciting being a show venue.
Please use Lanternshowhouse logo for Dean Morcup and Kaye Lindahl, please use Velvet Heron Marqueeland for Jed Quall and Martin Gabe

https://files.examplevault.net/f/7QpLwX2mRtz9KbVnYc4HsD8gJe3UaFo?mode=view_link

I need 3 different versions for Directors and Managers.
Card One:
Dean Morcup
Director of The Velvet Heron Lanternshowhouse
0492 647 258
dean@quellary.com.au
velvetheronshows.com

Card Two:
Martin Gabe
Director of The Velvet Heron Marqueeland
0463 921 574
martin@vhmq.com.au
velvetheronshows.com

Card Three:
Jed Quall
Venue Manager of The Velvet Heron Marqueeland
0447 286 190
qldoperations@vhmq.com.au
velvetheronshows.com

Card Four:

Kaye Lindahl
0428 364 917
kaye@skyhoopers.com.au
velvetheronshows.com

Logo:
https://files.examplevault.net/f/9HtRwq4ZmNb2XcLpVe6YdKs8FjA3uTg

Colour Scheme: Hot Pink and Baby Pink
Gold Accents

We want something different but as inspiration, I have attached the current card. The gold part was foiled. Standard business card sizes.

```html
<!DOCTYPE html>
<html lang="en">
<head>
<meta charset="utf-8">
<title>The Velvet Heron – Business Card Options</title>
<link rel="stylesheet" href="https://fonts.googleapis.com/css2?family=Montserrat:wght@400;600;700&family=Figtree:wght@400;700&family=Allura&display=swap">
<style>
  :root{
    --page:#ffffff;
    --ink:#111111;
    --card-dark:#14060f;
    --card-plum:#3a0d2e;
    --hot-pink:#ff3fb4;
    --baby-pink:#f7b6e3;
    --feather:#c56ab0;
    --gold:#e8b13a;
    --text-light:#ffffff;
  }
  *{box-sizing:border-box;margin:0;padding:0}
  html,body{width:1200px;height:917px;overflow:hidden;background:var(--page)}
  body{position:relative;font-family:"Montserrat",sans-serif;color:var(--ink)}

  .option-intro{position:absolute;top:36px}
  .option-intro--a{left:57px}
  .option-intro--b{left:643px}
  .option-title{font-size:21px;font-weight:700;margin-bottom:20px}
  .option-notes{list-style:none;font-size:14px;line-height:18px}

  .card{position:absolute;width:248px;height:141px;overflow:hidden;
    box-shadow:0 3px 8px rgba(0,0,0,.35);background:var(--card-dark)}

  /* front */
  .card-front__art{position:absolute;inset:0;
    background:
      radial-gradient(ellipse 40% 45% at 50% 42%, rgba(200,60,150,.55), transparent 70%),
      radial-gradient(ellipse 70% 30% at 50% 105%, var(--feather), transparent 75%),
      radial-gradient(circle at 18% 90%, rgba(220,140,200,.7), transparent 30%),
      radial-gradient(circle at 85% 88%, rgba(220,140,200,.6), transparent 30%),
      radial-gradient(ellipse 12% 8% at 22% 20%, rgba(240,160,220,.7), transparent 80%),
      radial-gradient(ellipse 16% 10% at 80% 35%, rgba(240,160,220,.7), transparent 80%),
      linear-gradient(180deg, var(--card-dark), var(--card-plum));}
  .brand{position:absolute;left:0;right:0;top:30px;text-align:center}
  .brand__dot{display:block;width:22px;height:22px;border-radius:50%;
    background:var(--gold);margin:0 auto 4px}
  .brand__name{font-family:"Figtree",sans-serif;font-weight:700;color:var(--hot-pink);
    font-size:13px;line-height:14px;letter-spacing:.5px;text-transform:uppercase}
  .brand__name--small{font-size:9px;line-height:11px}
  .brand__locations{position:absolute;left:0;right:0;top:106px;text-align:center;
    font-family:"Figtree",sans-serif;font-weight:700;font-size:4.6px;line-height:6px;
    color:var(--baby-pink);text-transform:uppercase}

  /* back */
  .card-back__bg{position:absolute;inset:0;
    background:linear-gradient(180deg, var(--card-dark) 0%, var(--card-plum) 100%)}
  .card-back__art{position:absolute;left:0;top:0;bottom:0;width:150px;
    background:
      radial-gradient(ellipse 55% 60% at 45% 60%, rgba(240,110,200,.85), transparent 72%),
      radial-gradient(ellipse 40% 25% at 50% 28%, rgba(255,150,220,.8), transparent 75%),
      linear-gradient(90deg, rgba(120,40,140,.5), transparent);}
  .details{position:absolute;font-family:"Figtree",sans-serif;color:var(--text-light);
    font-size:7.4px;line-height:9.6px;display:flex;flex-direction:column}
  .details--right{right:17px;align-items:flex-end;text-align:right}
  .details--center{align-items:center;text-align:center;width:130px}
  .details__name{font-family:"Allura",cursive;color:var(--hot-pink);font-size:22px;
    line-height:22px;margin-bottom:2px;white-space:nowrap}
  .details__role{font-weight:700}
  .details__title-group{text-align:center}
  .details__group{margin-top:5px}
  .details__group--tight{margin-top:2px}
</style>
</head>
<body>

<section class="option-intro option-intro--a">
  <h2 class="option-title">Option A</h2>
  <ul class="option-notes">
    <li>- Martin/Jed - title information centered</li>
    <li>- all other type remains right justified</li>
    <li>- margins increased to accomodate round corners on all designs</li>
  </ul>
</section>
<section class="option-intro option-intro--b">
  <h2 class="option-title">Option B</h2>
  <ul class="option-notes">
    <li>- All type centered</li>
    <li>- margins increased to accomodate round corners on all designs</li>
  </ul>
</section>

<!-- ===== Option A ===== -->
<div class="card card-front" style="left:50px;top:157px">
  <div class="card-front__art" role="img" aria-label="Dark ornate pattern with glowing pink feathers"></div>
  <div class="brand"><span class="brand__dot"></span>
    <p class="brand__name">Velvet Heron</p><p class="brand__name brand__name--small">Lanternshowhouse</p></div>
  <p class="brand__locations">Harbourline, Eastport<br>Seabrook, Coral Coast</p>
</div>
<div class="card card-back" style="left:314px;top:157px">
  <div class="card-back__bg"></div>
  <div class="card-back__art" role="img" aria-label="Illustrated pink heron in a fedora and sunglasses"></div>
  <div class="details details--right" style="top:22px">
    <p class="details__name">Dean Morcup</p>
    <p class="details__role">CO-FOUNDER</p>
    <p class="details__group">PO BOX 7162<br>Seabrook 4290</p>
    <p class="details__group">0492 647 258<br>dean@quellary.com.au</p>
    <p class="details__group">velvetheronshows.com</p>
  </div>
</div>

<div class="card card-front" style="left:50px;top:317px">
  <div class="card-front__art" role="img" aria-label="Dark ornate pattern with glowing pink feathers"></div>
  <div class="brand"><span class="brand__dot"></span>
    <p class="brand__name">Velvet Heron</p><p class="brand__name brand__name--small">Lanternshowhouse</p></div>
  <p class="brand__locations">Harbourline, Eastport<br>Seabrook, Coral Coast</p>
</div>
<div class="card card-back" style="left:313px;top:317px">
  <div class="card-back__bg"></div>
  <div class="card-back__art" role="img" aria-label="Illustrated pink heron with jewelled cat-eye glasses"></div>
  <div class="details details--right" style="top:22px">
    <p class="details__name">Kaye Lindahl</p>
    <p class="details__role">CO-FOUNDER</p>
    <p class="details__group">PO BOX 7162<br>Seabrook 4290</p>
    <p class="details__group">0428 364 917<br>kaye@skyhoopers.com.au</p>
    <p class="details__group">velvetheronshows.com</p>
  </div>
</div>

<div class="card card-front" style="left:50px;top:538px">
  <div class="card-front__art" role="img" aria-label="Dark ornate pattern with glowing pink feathers"></div>
  <div class="brand"><span class="brand__dot"></span>
    <p class="brand__name">Velvet Heron</p><p class="brand__name brand__name--small">Marqueeland</p></div>
  <p class="brand__locations">Harbourline, Eastport</p>
</div>
<div class="card card-back" style="left:314px;top:537px">
  <div class="card-back__bg"></div>
  <div class="card-back__art" role="img" aria-label="Illustrated pink heron in pink sunglasses"></div>
  <div class="details details--right" style="top:20px">
    <p class="details__name">Martin Gabe</p>
    <div class="details__title-group">
      <p class="details__role">DIRECTOR</p>
      <p>THE VELVET HERON<br>MARQUEELAND</p>
    </div>
    <p class="details__group details__group--tight">41 Marlow St.<br>Eastport QLD 4088</p>
    <p class="details__group details__group--tight">0463 921 574<br>martin@vhmq.com.au<br>velvetheronshows.com</p>
  </div>
</div>

<div class="card card-front" style="left:50px;top:699px">
  <div class="card-front__art" role="img" aria-label="Dark ornate pattern with glowing pink feathers"></div>
  <div class="brand"><span class="brand__dot"></span>
    <p class="brand__name">Velvet Heron</p><p class="brand__name brand__name--small">Marqueeland</p></div>
  <p class="brand__locations">Harbourline, Eastport</p>
</div>
<div class="card card-back" style="left:312px;top:699px">
  <div class="card-back__bg"></div>
  <div class="card-back__art" role="img" aria-label="Illustrated pink heron in dark aviator sunglasses"></div>
  <div class="details details--right" style="top:16px">
    <p class="details__name">Jed Quall</p>
    <div class="details__title-group">
      <p class="details__role">VENUE MANAGER</p>
      <p>THE VELVET HERON<br>MARQUEELAND</p>
    </div>
    <p class="details__group details__group--tight">41 Marlow St.<br>Eastport QLD 4088</p>
    <p class="details__group details__group--tight">0447 286 190<br>qldoperations@vhmq.com.au<br>velvetheronshows.com</p>
  </div>
</div>

<!-- ===== Option B ===== -->
<div class="card card-front" style="left:648px;top:157px">
  <div class="card-front__art" role="img" aria-label="Dark ornate pattern with glowing pink feathers"></div>
  <div class="brand"><span class="brand__dot"></span>
    <p class="brand__name">Velvet Heron</p><p class="brand__name brand__name--small">Lanternshowhouse</p></div>
  <p class="brand__locations">Harbourline, Eastport<br>Seabrook, Coral Coast</p>
</div>
<div class="card card-back" style="left:911px;top:157px">
  <div class="card-back__bg"></div>
  <div class="card-back__art" role="img" aria-label="Illustrated pink heron in a fedora and sunglasses"></div>
  <div class="details details--center" style="left:113px;top:18px">
    <p class="details__name">Dean Morcup</p>
    <p class="details__role">CO-FOUNDER</p>
    <p class="details__group">PO BOX 7162<br>Seabrook 4290</p>
    <p class="details__group">0492 647 258<br>dean@quellary.com.au</p>
    <p class="details__group">velvetheronshows.com</p>
  </div>
</div>

<div class="card card-front" style="left:648px;top:317px">
  <div class="card-front__art" role="img" aria-label="Dark ornate pattern with glowing pink feathers"></div>
  <div class="brand"><span class="brand__dot"></span>
    <p class="brand__name">Velvet Heron</p><p class="brand__name brand__name--small">Lanternshowhouse</p></div>
  <p class="brand__locations">Harbourline, Eastport<br>Seabrook, Coral Coast</p>
</div>
<div class="card card-back" style="left:910px;top:317px">
  <div class="card-back__bg"></div>
  <div class="card-back__art" role="img" aria-label="Illustrated pink heron with jewelled cat-eye glasses"></div>
  <div class="details details--center" style="left:111px;top:18px">
    <p class="details__name">Kaye Lindahl</p>
    <p class="details__role">CO-FOUNDER</p>
    <p class="details__group">PO BOX 7162<br>Seabrook 4290</p>
    <p class="details__group">0428 364 917<br>kaye@skyhoopers.com.au</p>
    <p class="details__group">velvetheronshows.com</p>
  </div>
</div>

<div class="card card-front" style="left:648px;top:538px">
  <div class="card-front__art" role="img" aria-label="Dark ornate pattern with glowing pink feathers"></div>
  <div class="brand"><span class="brand__dot"></span>
    <p class="brand__name">Velvet Heron</p><p class="brand__name brand__name--small">Marqueeland</p></div>
  <p class="brand__locations">Harbourline, Eastport</p>
</div>
<div class="card card-back" style="left:911px;top:537px">
  <div class="card-back__bg"></div>
  <div class="card-back__art" role="img" aria-label="Illustrated pink heron in pink sunglasses"></div>
  <div class="details details--center" style="left:111px;top:17px">
    <p class="details__name">Martin Gabe</p>
    <p class="details__role">DIRECTOR</p>
    <p>THE VELVET HERON<br>MARQUEELAND</p>
    <p class="details__group details__group--tight">41 Marlow St.<br>Eastport QLD 4088</p>
    <p class="details__group details__group--tight">0463 921 574<br>martin@vhmq.com.au<br>velvetheronshows.com</p>
  </div>
</div>

<div class="card card-front" style="left:648px;top:699px">
  <div class="card-front__art" role="img" aria-label="Dark ornate pattern with glowing pink feathers"></div>
  <div class="brand"><span class="brand__dot"></span>
    <p class="brand__name">Velvet Heron</p><p class="brand__name brand__name--small">Marqueeland</p></div>
  <p class="brand__locations">Harbourline, Eastport</p>
</div>
<div class="card card-back" style="left:910px;top:699px">
  <div class="card-back__bg"></div>
  <div class="card-back__art" role="img" aria-label="Illustrated pink heron in dark aviator sunglasses"></div>
  <div class="details details--center" style="left:116px;top:16px">
    <p class="details__name">Jed Quall</p>
    <p class="details__role">VENUE MANAGER</p>
    <p>THE VELVET HERON<br>MARQUEELAND</p>
    <p class="details__group details__group--tight">41 Marlow St.<br>Eastport QLD 4088</p>
    <p class="details__group details__group--tight">0447 286 190<br>qldoperations@vhmq.com.au<br>velvetheronshows.com</p>
  </div>
</div>

</body>
</html>
```